Bright LumaTrex & Equipments

I need to create full stationery design for the company; Business Card, Envelop, Letterheads, Calendar and email template.

Our company is specialized in the import and export of nutritional, pharmaceutical and cosmetics in addition to medical equipments.

These is no limitation on how to use colors within the design.

Target Market(s)

Global

Industry/Entity Type

Healthcare

Other font styles liked:
• a font close to logo. Letterhead body text to be different than the address text

Requirements
Nice to have
• We will have multiple locations so it is good to keep space for future addresses.
• Stationary requirements:
• Letterhead: A4
• Envelopes: 3 regular sizes : large, medium and small (i do not know the sizes)
• Colors: extracted from the logo

```html
<!DOCTYPE html>
<html lang="en">
<head>
<meta charset="utf-8">
<title>Bright LumaTrex &amp; Equipments — Letterhead</title>
<link href="https://fonts.googleapis.com/css2?family=Open+Sans:wght@400;700&family=Tinos:ital@0;1&display=swap" rel="stylesheet">
<style>
  :root{
    --bg:#ececec;
    --paper:#ffffff;
    --ink:#222222;
    --muted:#555555;
    --brand-blue:#2a9fd6;
    --brand-navy:#0c1a5b;
    --signature:#cfcfcf;
  }
  *{margin:0;padding:0;box-sizing:border-box}
  html,body{width:1200px;height:795px;overflow:hidden;background:var(--bg)}
  .letterhead{
    position:absolute;left:340px;top:30px;width:520px;height:735px;
    background:var(--paper);box-shadow:0 4px 18px rgba(0,0,0,.12);overflow:hidden;
  }
  .brand{position:absolute;left:44px;top:62px;display:flex;align-items:center;gap:8px}
  .brand-square{width:14px;height:14px;background:var(--brand-navy)}
  .brand-name{font-family:"Open Sans",sans-serif;font-weight:700;font-size:13px;color:var(--brand-blue);line-height:1.1}
  .contact{
    position:absolute;right:36px;top:40px;
    font-family:"Open Sans",sans-serif;font-style:normal;font-weight:400;
    font-size:6px;color:var(--muted);line-height:1.55;
  }
  .contact-line{display:flex;align-items:center;gap:4px}
  .contact-line svg{width:6px;height:6px;fill:var(--brand-navy)}
  .contact-address{margin-bottom:3px}
  .letter{
    position:absolute;left:78px;top:168px;width:370px;
    font-family:"Tinos",serif;font-size:9.6px;line-height:1.42;color:var(--ink);text-align:justify;
  }
  .salutation{margin-bottom:10px}
  .letter p{margin-bottom:12px}
  .closing{position:absolute;left:300px;top:470px;font-family:"Tinos",serif;font-size:9.6px;line-height:1.45;color:var(--ink)}
  .signature{width:80px;height:26px;margin:4px 0 2px;background:var(--signature);border-radius:3px}
  .edge-rule{position:absolute;right:0;bottom:0;width:4px;height:300px;background:var(--brand-navy)}
</style>
</head>
<body>
<main class="letterhead">
  <div class="brand">
    <div class="brand-square"></div>
    <div class="brand-name">Bright LumaTrex &amp; Equipments</div>
  </div>

  <address class="contact">
    <div class="contact-address">1870 Harbor Lane, Westford,<br>Oregon 97021</div>
    <div class="contact-line"><svg viewBox="0 0 10 10"><path d="M2 0h3l1 3-2 1a6 6 0 0 0 2 2l1-2 3 1v3c0 1-1 2-2 2A9 9 0 0 1 0 2c0-1 1-2 2-2z"/></svg>0740 555 0182</div>
    <div class="contact-line"><svg viewBox="0 0 10 10"><path d="M0 2h10v6H0zM0 2l5 4 5-4"/></svg>hello@lumatrex.com</div>
    <div class="contact-line"><svg viewBox="0 0 10 10"><circle cx="5" cy="5" r="5"/></svg>www.lumatrex.com</div>
  </address>

  <article class="letter">
    <div class="salutation">Gentlemen,</div>
    <p>Enclosed I have the honor to send you an article which I should be pleased if you would accept for the “Northern Review”. I am <i>desperately</i> pushed for money; and in the event of Mr. Halloran’s liking the “Landscape-Garden”, I would take it as an especial favor if you would mail me the amount due for it, so as to reach me here by the 21st, on which day I shall need it. Can you possibly oblige me in this? If you accept the paper I presume you will allow me your usual sum, whatever that is for similar contributions—but I set no price—leaving all to your own liberality. The piece will make 8 of your pages and rather more.</p>
    <p>Will you be kind enough to put the best possible interpretation upon my behavior while in N-York? You must have conceived a <i>queer</i> idea of me—but the simple truth is that Whitcombe would insist upon <i>the juleps</i>, and I knew not what I was either doing or saying. The Review of Dane which I offered you was deficient in a ½ page of commencement, which I had written to supersede the old beginning, and which gave the article the character of a general and retrospective review. No wonder you did not take it—I would have been very much mortified if you had. I hope to see you at some future time, under better auspices.</p>
  </article>

  <div class="closing">
    In the meantime I remain<br>
    Yours very truly,
    <div class="signature" role="img" aria-label="Handwritten signature of Edwin A. Pell"></div>
    Edwin A. Pell
  </div>

  <div class="edge-rule"></div>
</main>
</body>
</html>
```